Medical Device Packaging Project 2 of 5

We are a medical device startup company needing packaging for a total of 5 device brands. This is posting 2 of 5 and the device name is "Velmora"

Velmora is an intraocular lens for use in cataract surgery. The target market is Chinese ophthalmologists. The box should be sophisticated and upmarket.

The company name is Brindle Optics, I have included the logo in the uploaded files section. You should include the logo on the box.

I have uploaded a sample lens boxes from other companies that demonstrate the information needed to be contained on the box in terms of address, warnings, symbols, etc.

I have also uploaded the blank dieline of the boxes

You are welcome and encouraged to also submit to projects 1, 3, 4, and 5 as well. The same rules and expectations apply.

Requirements
Should not have
• Should not have any images of an eye or any bionic/futuristic feel to the design
• Note that the vantiscope box is for text reference only. You may use the lens image but the futuristic/bionic look is NOT what we are going for with this brand. It should be traditional upmarket medical device artwork.

```html
<!DOCTYPE html>
<html lang="en">
<head>
<meta charset="utf-8">
<title>Velmora — Intraocular Lens Carton Dieline</title>
<link href="https://fonts.googleapis.com/css2?family=Montserrat:wght@400;500;600;700;800&family=Arimo:wght@400;700&family=Tinos&display=swap" rel="stylesheet">
<style>
  :root{
    --navy:#14497e;
    --navy-text:#1d4b80;
    --fold:#2a5d92;
    --paper:#ffffff;
    --rule:#c9d3de;
    --dim:#333333;
    --lens-light:#f3f6f8;
    --lens-mid:#d6e1e8;
    --lens-edge:#b9c9d4;
  }
  *{margin:0;padding:0;box-sizing:border-box}
  html,body{width:1064px;height:1200px;overflow:hidden;background:#fff}
  body{position:relative;font-family:"Montserrat",Arial,sans-serif;color:var(--navy-text)}
  .dieline{position:absolute;left:0;top:0}
  .abs{position:absolute}
  .dim{font-family:"Tinos","Times New Roman",serif;font-size:15px;color:var(--dim);white-space:nowrap}
  .dim.vertical{transform:rotate(-90deg);transform-origin:center}

  .contact{left:495px;top:142px;width:290px;transform:rotate(180deg);color:#fff;font-family:"Arimo",Arial,sans-serif;font-weight:700;font-size:10.5px;line-height:13px;text-align:right;white-space:nowrap}

  .brand-name{font-weight:600;letter-spacing:1px;white-space:nowrap;display:flex;align-items:center;gap:8px}
  .brand-dot{width:10px;height:10px;border-radius:50%;background:currentColor;display:inline-block;flex:none}
  .brand-front{left:290px;top:272px;font-size:17px;color:var(--navy-text)}
  .brand-band{left:410px;top:648px;width:260px;justify-content:center;font-size:20px;color:#fff}
  .brand-side{left:780px;top:480px;width:180px;justify-content:center;font-size:18px;color:#fff;transform:rotate(-90deg)}

  .title-front{left:633px;top:232px;width:150px;font-weight:800;font-size:28px;line-height:32px;text-align:center;white-space:nowrap}
  .tagline{left:633px;top:269px;width:148px;border-top:1.5px solid var(--navy-text);border-bottom:1.5px solid var(--navy-text);padding:8px 0;text-align:center;font-size:11.5px;line-height:13px}
  .tagline b{font-weight:700}

  .lens-art{background:radial-gradient(ellipse at 50% 50%,var(--lens-light) 0%,var(--lens-mid) 70%,var(--lens-edge) 100%);border-radius:40px}
  .lens-edge-view{background:linear-gradient(180deg,var(--lens-light),var(--lens-mid) 50%,var(--lens-edge));border-radius:6px}

  .edge-claim{left:290px;top:607px;color:#fff;font-weight:700;font-size:13px;letter-spacing:.2px}

  .title-back{left:569px;top:750px;font-weight:800;font-size:24px;letter-spacing:.3px}
  .languages{left:569px;top:786px;width:232px;font-family:"Arimo",Arial,sans-serif;font-size:8.4px;line-height:8.9px}
  .languages p{margin-bottom:6px;white-space:nowrap}

  .symbols{display:flex;align-items:center;gap:10px}
  .symbols-back{left:569px;top:1070px;color:var(--navy-text)}
  .symbols-side{left:858px;top:290px;transform:rotate(-90deg);color:#fff}
  .sterile-box{display:flex;border:1px solid currentColor;font-size:6.5px;font-weight:700;line-height:10px}
  .sterile-box span{padding:0 3px}
  .sterile-box span+span{border-left:1px solid currentColor}
</style>
</head>
<body>

<svg class="dieline" width="1064" height="1200" viewBox="0 0 1064 1200" aria-hidden="true">
  <polygon fill="var(--navy)" points="148,88 252,88 273,64 806,64 828,88 958,88 958,193 828,193 806,210 273,210 252,193 148,193"/>
  <path fill="var(--navy)" d="M273,210 H76 Q52,210 52,234 V561 Q52,585 76,585 H273 Z"/>
  <path fill="var(--navy)" d="M806,210 H1004 Q1028,210 1028,234 V561 Q1028,585 1004,585 H806 Z"/>
  <line x1="127" y1="210" x2="127" y2="585" stroke="var(--fold)" stroke-width="1"/>
  <line x1="952" y1="210" x2="952" y2="585" stroke="var(--fold)" stroke-width="1"/>
  <rect x="273" y="210" width="533" height="375" fill="var(--paper)"/>
  <polygon fill="var(--navy)" points="148,600 252,600 273,585 806,585 828,600 958,600 958,710 828,710 806,732 273,732 252,710 148,710"/>
  <rect x="273.5" y="732.5" width="532" height="374" fill="var(--paper)" stroke="var(--rule)" stroke-width="1"/>
  <polygon fill="var(--navy)" points="273,1107 806,1107 800,1155 280,1155"/>
</svg>

<div class="abs dim" style="left:195px;top:33px">35mm</div>
<div class="abs dim" style="left:497px;top:39px">128mm</div>
<div class="abs dim" style="left:848px;top:33px">35mm</div>
<div class="abs dim vertical" style="left:101px;top:128px">35mm</div>
<div class="abs dim" style="left:68px;top:175px">18mm</div>
<div class="abs dim" style="left:970px;top:175px">18mm</div>
<div class="abs dim vertical" style="left:11px;top:382px">90mm</div>
<div class="abs dim vertical" style="left:101px;top:634px">35mm</div>
<div class="abs dim vertical" style="left:209px;top:933px">90mm</div>
<div class="abs dim vertical" style="left:209px;top:1128px">12mm</div>

<div class="abs contact">
  Here we would write your contact info etc<br>
  which I do not know for now<br>
  website: www.brindleoptics.com &nbsp;email: info@brindleoptics.com
</div>

<div class="abs brand-name brand-front"><span class="brand-dot"></span>BRINDLE OPTICS</div>
<div class="abs title-front">VELMORA</div>
<div class="abs tagline"><b>Intraocular lens</b> for use<br>in cataract surgery</div>
<div class="abs lens-art" role="img" aria-label="Intraocular lens with two curved haptics, front view" style="left:362px;top:300px;width:262px;height:146px"></div>
<div class="abs lens-edge-view" role="img" aria-label="Intraocular lens, side profile" style="left:364px;top:530px;width:356px;height:16px"></div>

<div class="abs symbols symbols-side">
  <div class="sterile-box"><span>STERILE</span><span>EO</span></div>
  <svg width="16" height="14" viewBox="0 0 16 14"><polygon points="8,1 15,13 1,13" fill="none" stroke="currentColor" stroke-width="1"/><line x1="8" y1="5" x2="8" y2="9" stroke="currentColor"/></svg>
  <svg width="15" height="15" viewBox="0 0 15 15"><circle cx="7.5" cy="7.5" r="6.5" fill="none" stroke="currentColor"/><text x="7.5" y="10.5" font-size="8" text-anchor="middle" fill="currentColor" font-family="Montserrat">2</text><line x1="3" y1="12" x2="12" y2="3" stroke="currentColor"/></svg>
  <svg width="15" height="15" viewBox="0 0 15 15"><circle cx="7.5" cy="7.5" r="6.5" fill="none" stroke="currentColor"/><line x1="3" y1="12" x2="12" y2="3" stroke="currentColor"/><rect x="4.5" y="5" width="6" height="5" fill="none" stroke="currentColor" stroke-width=".8"/></svg>
  <svg width="15" height="15" viewBox="0 0 15 15"><circle cx="7.5" cy="7.5" r="6.5" fill="none" stroke="currentColor"/><line x1="3" y1="12" x2="12" y2="3" stroke="currentColor"/><circle cx="7.5" cy="7.5" r="2.5" fill="none" stroke="currentColor" stroke-width=".8"/></svg>
</div>
<div class="abs brand-name brand-side"><span class="brand-dot"></span>BRINDLE OPTICS</div>

<div class="abs edge-claim">WITH 360° SQUARE EDGE</div>
<div class="abs brand-name brand-band"><span class="brand-dot"></span>BRINDLE OPTICS</div>

<div class="abs lens-art" role="img" aria-label="Intraocular lens with two curved haptics, vertical front view" style="left:302px;top:752px;width:138px;height:332px"></div>
<div class="abs lens-edge-view" role="img" aria-label="Intraocular lens, vertical side profile" style="left:513px;top:756px;width:15px;height:324px"></div>

<div class="abs title-back">VELMORA</div>
<div class="abs languages">
  <p>Contains one sterile intraocular lens<br>Do not use if the packaging is damaged<br>Do not resterilize</p>
  <p>Bevat één steriele intraoculaire lens<br>Niet gebruiken als de verpakking beschadigd is<br>Niet opnieuw steriliseren</p>
  <p>Contient une lentille intraoculaire stérile<br>Ne pas utiliser si l'emballage est endommagé<br>Ne pas restériliser</p>
  <p>Enthält eine sterile intraokulare Linse<br>Nicht verwenden, wenn die Verpackung beschädigt ist<br>Nicht resterilisieren</p>
  <p>Periéchei éna aposteiroméno endofthálmia fakó OR<br>Περιέχει ένα αποστειρωμένο ενδοφθάλμιο φακό<br>Μην το χρησιμοποιείτε εάν η συσκευασία έχει υποστεί ζημιά<br>OR Min to chrisimopoieíte eán i syskevasía échei ypostei zimiá<br>Μην επαναποστειρώνετε &nbsp;OR Min epanaposteirónete</p>
  <p>Contiene una lente intraoculare sterile<br>Non usare se la confezione è danneggiata<br>Non risterilizzare</p>
  <p>Contém uma lente intra-ocular esterilizada<br>Não use se a embalagem está danificada<br>Não reesterilize</p>
  <p>Contiene una lente intraocular estéril<br>No utilizar si el envase está dañado<br>No vuelva a esterilizar</p>
</div>

<div class="abs symbols symbols-back">
  <div class="sterile-box"><span>STERILE</span><span>EO</span></div>
  <svg width="20" height="18" viewBox="0 0 20 18"><polygon points="10,1 19,17 1,17" fill="none" stroke="currentColor" stroke-width="1"/><line x1="10" y1="6" x2="10" y2="12" stroke="currentColor"/></svg>
  <svg width="18" height="18" viewBox="0 0 18 18"><circle cx="9" cy="9" r="8" fill="none" stroke="currentColor"/><text x="9" y="12.5" font-size="10" text-anchor="middle" fill="currentColor" font-family="Montserrat">2</text><line x1="3.5" y1="14.5" x2="14.5" y2="3.5" stroke="currentColor"/></svg>
  <svg width="18" height="18" viewBox="0 0 18 18"><circle cx="9" cy="9" r="8" fill="none" stroke="currentColor"/><line x1="3.5" y1="14.5" x2="14.5" y2="3.5" stroke="currentColor"/><rect x="5.5" y="6" width="7" height="6" fill="none" stroke="currentColor" stroke-width=".8"/></svg>
  <svg width="18" height="18" viewBox="0 0 18 18"><circle cx="9" cy="9" r="8" fill="none" stroke="currentColor"/><line x1="3.5" y1="14.5" x2="14.5" y2="3.5" stroke="currentColor"/><circle cx="9" cy="9" r="3" fill="none" stroke="currentColor" stroke-width=".8"/></svg>
</div>

</body>
</html>
```